LH Business Card NEEDED

Lumen Harbour is a finance brokering company that provide lending advise to consumer, business, corporate, and property developer for all their financing needs.

We source and match customer needs in Home Loan, Business Loan, Commercial Property Loan, Assets Finance, and other banking related services. It is a market with full of loans! But we specialise in more complex loan structure and our client base are more business and corporate level. Our suppliers are Banks and large Financial Institution where these business card will go to.

We have a great deal of Asian clients, therefore the card need to also include Chinese language together with English.

Refer to attached file for logo and content requirements.

We are looking for designs with the following ingredients:
* Innovative & Creative
* Professional
* Trust & Security

Please pick colours that will compliment the colours of the company logo.

Please provide a unique design, for example the edge of the card is rounded or corner cut off.
Updates

Company logo uploaded.

Please commence submitting your design.

Target Market(s)

Target audiences are businessmen, corporate, and property developer. And also a great deal of Chinese clients.

Industry/Entity Type

Finance

Contact Information for Business Card

Lumen Harbour Pty. Ltd.
Morris Okafor
Director
Suite 42, 7-9 Pellow St. Dunmore NSW 2738

Requirements
Must have
• Double sided design

```html
<!DOCTYPE html>
<html lang="en">
<head>
<meta charset="utf-8">
<title>Lumen Harbour Business Card</title>
<link href="https://fonts.googleapis.com/css2?family=Raleway:wght@300;400&family=Noto+Serif+TC:wght@400&display=swap" rel="stylesheet">
<style>
  :root {
    --stage: #2a2a2c;
    --navy-light: #2f4f7d;
    --navy: #1f3a63;
    --navy-dark: #142846;
    --ink: #e4e8ef;
    --ink-soft: #b7c2d3;
    --rule: #8a9ab3;
    --mark: #c9cdd4;
  }
  * { margin: 0; padding: 0; box-sizing: border-box; }
  html, body { width: 1200px; height: 901px; overflow: hidden; }
  body {
    background: var(--stage);
    font-family: "Raleway", sans-serif;
    position: relative;
  }
  .card {
    position: absolute;
    width: 580px;
    height: 334px;
    border-radius: 26px;
    background: radial-gradient(ellipse at 40% 30%, var(--navy-light) 0%, var(--navy) 50%, var(--navy-dark) 100%);
    color: var(--ink);
  }
  .card--front { left: 70px; top: 90px; }
  .card--back { left: 550px; top: 475px; }

  /* front */
  .front-brand {
    position: absolute; left: 0; right: 0; top: 62px;
    display: flex; flex-direction: column; align-items: center;
  }
  .brand-dot {
    width: 74px; height: 74px; border-radius: 50%;
    background: var(--mark);
    margin-bottom: 22px;
  }
  .brand-name {
    font-weight: 300; font-size: 22px; letter-spacing: 9px;
    text-transform: uppercase; color: var(--ink);
  }
  .brand-rule {
    width: 250px; height: 1px; background: var(--rule); margin: 10px 0 8px;
  }
  .brand-chinese {
    font-family: "Noto Serif TC", serif; font-size: 18px; letter-spacing: 4px; color: var(--ink);
  }
  .brand-tagline {
    margin-top: 10px; font-weight: 300; font-size: 14px; letter-spacing: 3px; color: var(--ink-soft);
  }

  /* back */
  .person { position: absolute; left: 46px; top: 50px; }
  .person-name { font-size: 19px; font-weight: 400; letter-spacing: 0.5px; }
  .person-name-zh { font-family: "Noto Serif TC", serif; font-size: 16px; margin-top: 4px; }
  .person-role { font-size: 13px; margin-top: 14px; color: var(--ink-soft); }
  .person-role-zh { font-family: "Noto Serif TC", serif; font-size: 13px; margin-top: 3px; color: var(--ink-soft); }
  .back-rule {
    position: absolute; left: 30px; top: 196px; width: 300px; height: 1px; background: var(--rule);
  }
  .contact {
    position: absolute; left: 80px; top: 220px;
    display: grid; grid-template-columns: 70px auto; row-gap: 6px;
    font-size: 15px; font-weight: 300;
  }
  .contact dt { color: var(--ink-soft); }
  .back-brand {
    position: absolute; right: 44px; top: 64px;
    display: flex; flex-direction: column; align-items: center;
  }
  .back-brand .brand-dot { width: 92px; height: 92px; margin-bottom: 12px; }
  .back-brand .brand-name { font-size: 13px; letter-spacing: 4px; }
</style>
</head>
<body>
  <section class="card card--front" aria-label="Card front">
    <div class="front-brand">
      <div class="brand-dot"></div>
      <div class="brand-name">Lumen Harbour</div>
      <div class="brand-rule"></div>
      <div class="brand-chinese">明港通</div>
      <div class="brand-tagline">Lend With Clarity</div>
    </div>
  </section>

  <section class="card card--back" aria-label="Card back">
    <div class="person">
      <div class="person-name">Morris Okafor</div>
      <div class="person-name-zh">莫里斯</div>
      <div class="person-role">Director</div>
      <div class="person-role-zh">董事</div>
    </div>
    <div class="back-rule"></div>
    <dl class="contact">
      <dt>Mobile</dt><dd>0412 555 019</dd>
      <dt>Email</dt><dd>info@lumenharbour.com</dd>
      <dt>Web</dt><dd>www.lumenharbour.com</dd>
    </dl>
    <div class="back-brand">
      <div class="brand-dot"></div>
      <div class="brand-name">Lumen Harbour</div>
    </div>
  </section>
</body>
</html>
```